Chartered Professional Accounting Firm Needs a Business Card Design

We need a card design for an accounting firm based in Toronto, Ontario. The firm name is Leo Dart Professional Corporation. The owner of the firm is a chartered professional accountant and a certified general accountant. Services of the firm include 60% tax preparation and consulting and 40% financial statements for corporation year-end. We would like a modern design. The color could be black, white, gray, blue or other color to bring more confidence to clients. The logo of the firm should be included in the design. Thanks

Name: Leo Dart, CPA, CGA Address: 47 Amberfield Cres. Richmond Hill, ON M3K 7P2 Telephone: (416) 555-0137 Fax:(416) 555-0192 Email: leo@leodart.example

Accounting

```html
<!DOCTYPE html>
<html lang="en">
<head>
<meta charset="utf-8">
<title>Leo Dart Professional Corporation — Business Card</title>
<link rel="stylesheet" href="https://fonts.googleapis.com/css2?family=Cinzel:wght@600;700&family=Lato:wght@400;700&display=swap">
<style>
  :root {
    --navy: #2f308c;
    --navy-deep: #25267a;
    --navy-light: #3d3fa6;
    --paper: #ffffff;
    --paper-shade: #f1f1f3;
    --ink: #3a3a3a;
    --rule: #9a9aa0;
    --edge-gray: #a9a9ad;
    --backdrop: #e6e6e8;
  }
  * { box-sizing: border-box; margin: 0; padding: 0; }
  html, body {
    width: 1200px; height: 871px; overflow: hidden;
    background: var(--backdrop);
    font-family: "Lato", sans-serif;
  }
  .card {
    position: absolute;
    width: 540px; height: 310px;
    border-radius: 3px;
    overflow: hidden;
    box-shadow: 0 6px 18px rgba(0,0,0,.18);
  }

  /* Front */
  .card--front {
    left: 70px; top: 110px;
    background: linear-gradient(135deg, var(--navy-light) 0%, var(--navy) 45%, var(--navy-deep) 100%);
  }
  .front-decor {
    position: absolute; right: 50px; top: 40px;
    width: 170px; height: 150px;
    border: 3px solid rgba(255,255,255,.06);
    background: rgba(255,255,255,.04);
  }
  .brand { position: absolute; display: flex; align-items: flex-start; gap: 12px; }
  .brand__mark { width: 38px; height: 38px; border: 3px solid currentColor; flex: none; margin-top: 2px; }
  .brand__name {
    font-family: "Cinzel", serif; font-weight: 700;
    font-size: 27px; line-height: 1; letter-spacing: .5px;
  }
  .brand__line {
    font-family: "Lato", sans-serif; font-size: 10.5px;
    letter-spacing: 1px; text-transform: uppercase; line-height: 1.25;
  }
  .brand__line--strong { font-weight: 700; font-size: 11.5px; margin-top: 3px; }
  .card--front .brand { left: 36px; bottom: 48px; color: #e6e7f5; }

  /* Back */
  .card--back {
    left: 590px; top: 440px;
    background: linear-gradient(180deg, var(--paper) 0%, var(--paper) 60%, var(--paper-shade) 100%);
  }
  .card--back .brand { left: 60px; top: 26px; color: var(--navy); }
  .card--back .brand__line { color: var(--ink); font-size: 9.5px; }
  .card--back .brand__line--strong { color: var(--navy); font-size: 10.5px; }

  .back-rule {
    position: absolute; left: 28px; right: 30px; top: 112px;
    height: 1px; background: var(--rule);
  }
  .address {
    position: absolute; left: 28px; top: 138px;
    font-size: 12px; letter-spacing: 1.6px; line-height: 2.1; color: var(--ink);
  }
  .holder {
    position: absolute; right: 30px; top: 148px; text-align: right;
    font-family: "Cinzel", serif; font-weight: 600;
    font-size: 19px; letter-spacing: 3px; color: var(--navy);
  }
  .holder-rule {
    position: absolute; right: 30px; top: 182px; width: 250px;
    height: 1px; background: var(--rule);
  }
  .contacts {
    position: absolute; right: 30px; top: 196px; list-style: none;
    font-size: 12.5px; letter-spacing: 1.6px; color: var(--ink);
  }
  .contacts li { display: flex; justify-content: flex-end; align-items: center; gap: 14px; height: 25px; }
  .contacts svg { width: 15px; height: 15px; fill: none; stroke: var(--navy); stroke-width: 1.6; }
  .back-band { position: absolute; left: 0; right: 0; bottom: 0; height: 9px; display: flex; }
  .back-band__gray { flex: 1; background: var(--edge-gray); }
  .back-band__blue { flex: 1; background: var(--navy); }
</style>
</head>
<body>
  <section class="card card--front" aria-label="Card front">
    <div class="front-decor"></div>
    <div class="brand">
      <span class="brand__mark"></span>
      <div>
        <div class="brand__name">LEO DART</div>
        <div class="brand__line brand__line--strong">Professional Corporation</div>
        <div class="brand__line">Chartered Professional Accountant</div>
        <div class="brand__line">Certified General Accountant</div>
      </div>
    </div>
  </section>

  <section class="card card--back" aria-label="Card back">
    <div class="brand">
      <span class="brand__mark"></span>
      <div>
        <div class="brand__name">LEO DART</div>
        <div class="brand__line brand__line--strong">Professional Corporation</div>
        <div class="brand__line">Chartered Professional Accountant</div>
        <div class="brand__line">Certified General Accountant</div>
      </div>
    </div>
    <div class="back-rule"></div>
    <address class="address" style="font-style:normal">
      47 Amberfield Cres.<br>Richmond Hill<br>ON M3K 7P2
    </address>
    <div class="holder">Leo Dart, CPA, CGA</div>
    <div class="holder-rule"></div>
    <ul class="contacts">
      <li>(416) 555-0137
        <svg viewBox="0 0 16 16" aria-hidden="true"><path d="M2 6c0-2 2-3 6-3s6 1 6 3l-2 1-1-2H5L4 7z"/><rect x="3.5" y="8" width="9" height="5" rx="1"/></svg>
      </li>
      <li>(416) 555-0192
        <svg viewBox="0 0 16 16" aria-hidden="true"><rect x="4" y="2" width="8" height="4"/><rect x="2" y="6" width="12" height="6" rx="1"/><rect x="4.5" y="10" width="7" height="4"/></svg>
      </li>
      <li>leo@leodart.example
        <svg viewBox="0 0 16 16" aria-hidden="true"><rect x="2" y="4" width="12" height="8"/><path d="M2 4l6 5 6-5"/></svg>
      </li>
    </ul>
    <div class="back-band"><span class="back-band__gray"></span><span class="back-band__blue"></span></div>
  </section>
</body>
</html>
```